Commercial Real Estate Appraisal Company needs a postcard design

We need a postcard design for a commercial real estate company based out of Ballston Lake, New York called "Northfield Appraisers".

Northfield Appraisers, LLC., provides high quality commercial appraisal and real estate consulting services to our clients. Our company provides appraisal services for financial lending institutions, real estate developers, local municipalities, attorney’s, private individuals and businesses. Significant capital expenditures were made to ensure we can provide top of the line data research and research publications, as well as, generate our reports with industry leading appraisal software for increased accuracy and efficiency.

Services we provide

Advisory & Consulting Services, Net Lease Valuation, Capitalization Rate Consultation, Operating Expense Consultation, Discounted Cash Flow Analysis, Portfolio Valuation, Expert Witness Services, Property and Comparable Analyses, Financial Feasibility Studies, Property Tax Services, Going Concern Valuations, Real Estate Due Diligence Analyses, Highest and Best Use Studies, Real Estate Valuation, Lease Versus Purchase Analyses, Rent Arbitration and Consultation, Market Rent Analyses, Sale Lease-Backs Analysis, Market Studies, Site Inspections, Divorce Proceedings, Probate / Estate Matters

Please save room on the card for postage and addressing

Industry/Entity Type

Real Estate

```html
<!DOCTYPE html>
<html lang="en">
<head>
<meta charset="utf-8">
<title>Northfield Appraisers – Postcard</title>
<link href="https://fonts.googleapis.com/css2?family=Lato:wght@300;400;700&display=swap" rel="stylesheet">
<style>
  :root {
    --backdrop: #1c1c1c;
    --card: #ffffff;
    --ink: #1f2430;
    --ink-soft: #5a5f68;
    --phone-grey: #4a4d52;
    --accent-blue: #1b6fc2;
    --navy: #1e2a44;
    --stamp-top: #f4f4f4;
    --stamp-bottom: #cfcfd1;
    --photo-light: #e9ecea;
    --photo-mid: #8c9aa3;
    --photo-dark: #2b333b;
  }
  * { margin: 0; padding: 0; box-sizing: border-box; }
  html, body { width: 1200px; height: 750px; overflow: hidden; }
  body {
    background: var(--backdrop);
    font-family: "Lato", Arial, sans-serif;
    position: relative;
  }

  /* ---------- Address side ---------- */
  .card-back {
    position: absolute; left: 144px; top: 52px;
    width: 603px; height: 392px;
    background: var(--card);
    box-shadow: 0 6px 18px rgba(0,0,0,.55);
  }
  .card-back .upper {
    position: absolute; left: 0; top: 0; width: 100%; height: 173px;
    background: linear-gradient(#ffffff 70%, #f1f1f2);
    border-bottom: 1px solid #e6e6e6;
  }
  .brand {
    position: absolute; display: flex; align-items: center; gap: 8px;
    color: var(--navy); font-weight: 700; white-space: nowrap;
  }
  .brand .mark { background: var(--navy); flex: none; }
  .card-back .brand { left: 44px; top: 98px; font-size: 17px; }
  .card-back .brand .mark { width: 14px; height: 14px; }

  .services { position: absolute; left: 264px; top: 35px; width: 220px; }
  .services h2 {
    font-size: 17px; font-weight: 700; color: var(--ink);
    margin: 0 0 3px 7px;
  }
  .services p {
    font-size: 7.2px; line-height: 9.3px; color: var(--ink-soft);
    text-align: justify;
  }
  .stamp-box {
    position: absolute; left: 507px; top: 11px; width: 87px; height: 85px;
    background: linear-gradient(var(--stamp-top), var(--stamp-bottom));
  }
  .contact { position: absolute; left: 22px; top: 228px; }
  .phone {
    display: flex; align-items: center; gap: 4px;
    margin-left: 24px; font-size: 24px; color: var(--phone-grey);
  }
  .phone svg { width: 30px; height: 30px; }
  .web {
    margin-top: 6px; display: inline-block;
    background: var(--accent-blue); color: #fff;
    font-size: 14px; padding: 3px 6px; width: 224px; text-align: center;
  }

  /* ---------- Picture side ---------- */
  .card-front {
    position: absolute; left: 424px; top: 256px;
    width: 647px; height: 421px;
    background: var(--card);
    box-shadow: 0 6px 22px rgba(0,0,0,.6);
    overflow: hidden;
  }
  .photo {
    position: absolute; left: 0; top: 0; width: 100%; height: 307px;
    background:
      radial-gradient(ellipse at 72% 20%, rgba(255,250,230,.95), transparent 45%),
      linear-gradient(180deg, var(--photo-light) 0%, var(--photo-mid) 45%, var(--photo-dark) 100%);
  }
  .badge-bg {
    position: absolute; left: 433px; top: 246px;
    width: 120px; height: 120px; border-radius: 50%; background: var(--card);
  }
  .card-front .brand { left: 392px; top: 354px; font-size: 17px; }
  .card-front .brand .mark { width: 14px; height: 14px; }
  .headline {
    position: absolute; left: 28px; top: 316px;
    font-size: 26px; font-weight: 300; color: var(--ink); letter-spacing: .2px;
  }
  .about {
    position: absolute; left: 28px; top: 348px; width: 312px;
    font-size: 7.2px; line-height: 9px; color: var(--ink-soft); text-align: justify;
  }
  .about strong { color: var(--ink); font-weight: 700; }
</style>
</head>
<body>

  <section class="card-back" aria-label="Postcard address side">
    <div class="upper">
      <div class="brand"><span class="mark"></span>Northfield Appraisers</div>

      <div class="services">
        <h2>Services we provide</h2>
        <p>Advisory &amp; Consulting Services, Net Lease Valuation, Capitalization Rate Consultation, Operating Expense Consultation, Discounted Cash Flow Analysis, Portfolio Valuation, Expert Witness Services, Property and Comparable Analyses, Financial Feasibility Studies, Property Tax Services, Going Concern Valuations, Real Estate Due Diligence Analyses, Highest and Best Use Studies, Real Estate Valuation, Lease Versus Purchase Analyses, Rent Arbitration and Consultation, Market Rent Analyses, Sale Lease-Backs Analysis, Market Studies, Site Inspections, Divorce Proceedings, Probate / Estate</p>
      </div>

      <div class="stamp-box" aria-label="Postage area"></div>
    </div>

    <div class="contact">
      <div class="phone">
        <svg viewBox="0 0 30 30" aria-hidden="true">
          <circle cx="15" cy="15" r="15" fill="var(--accent-blue)"/>
          <path d="M10.5 8.5c.6-.6 1.5-.5 1.9.2l1.4 2.3c.3.6.2 1.3-.3 1.7l-1 .8c.8 1.8 2.2 3.2 4 4l.8-1c.4-.5 1.1-.6 1.7-.3l2.3 1.4c.7.4.8 1.3.2 1.9l-1.2 1.2c-.8.8-2 1-3 .5-3.4-1.6-6-4.2-7.6-7.6-.5-1-.3-2.2.5-3z" fill="#fff"/>
        </svg>
        518.555.0147
      </div>
      <div class="web">www.NorthfieldAppraisers.com</div>
    </div>
  </section>

  <section class="card-front" aria-label="Postcard picture side">
    <div class="photo" role="img" aria-label="Photograph of business people talking and reviewing papers in a bright glass-walled office"></div>
    <div class="badge-bg"></div>
    <div class="brand"><span class="mark"></span>Northfield Appraisers</div>

    <h1 class="headline">IS TIME TO GOOD BUSINESS</h1>
    <p class="about"><strong>Northfield Appraisers, LLC.</strong>, provides high quality commercial appraisal and real estate consulting services to our clients. Our company provides appraisal services for financial lending institutions, real estate developers, local municipalities, attorney’s, private individuals and businesses. Significant capital expenditures were made to ensure we can provide top of the line data research and research publications, as well as, generate our reports with industry leading appraisal software for increased accuracy and efficiency.</p>
  </section>

</body>
</html>
```